Chinese Artwork Gallery and Tea House need website design

This is a challenging website design, as the styles combines contemporary layout infused with oriental artwork style. Our company run a oriental gallery/tea house from Sydney, specialising selling oriental antique replicate such as terra-cotta warriors, porcelain vases, bronze cups, traditional Chinese painting and calligraphy, tea and tea sets. The colour scheme will incorporate the existing gold, red and black being used for our logo.

Please include in the homepage a section with large sliding image to showcase individual antique pieces, as well as image to link to 6 categories of products we are selling in retail store and online store which are Porcelain, Bronze, Terra Cotta, Painting and Calligraphy, Chinese Artwork, Tea & Tea Sets. The home page needs to highlight our brand and the design pattern we have included in the logo design. Colour wise, red, black, gold and white. I hope above helps.

```html
<!DOCTYPE html>
<html lang="en">
<head>
<meta charset="utf-8">
<title>Lanxi Gallery &amp; Tea House</title>
<link href="https://fonts.googleapis.com/css2?family=Lato:wght@300;400;700&display=swap" rel="stylesheet">
<style>
:root{
  --red:#8c0000;
  --red-dark:#7a0000;
  --text-red:#8b1616;
  --gold:#c9a227;
  --gold-dark:#a8831a;
  --ink:#222;
  --grey:#555;
  --bg:#f2f2f2;
  --white:#fff;
  --line:#d8d8d8;
  --green:#8cc63f;
}
*{margin:0;padding:0;box-sizing:border-box}
html,body{width:727px;height:1200px;overflow:hidden}
body{font-family:"Lato",sans-serif;background:var(--bg);color:var(--ink);position:relative}
.abs{position:absolute}
.topbar{left:0;top:0;width:727px;height:16px;background:#1a1a1a;color:#fff;font-size:6.5px;font-weight:700}
.topbar .links{right:116px;top:4px}
.topbar .links span{margin:0 3px}
.header{left:0;top:16px;width:727px;height:116px;background:var(--red)}
.brand{left:98px;top:26px;display:flex;align-items:center;gap:6px}
.brand .mark{width:10px;height:10px;background:var(--gold)}
.brand .name{color:var(--gold);font-size:12px;letter-spacing:3px;font-weight:400}
.search{left:416px;top:22px;width:140px;height:18px;background:#fff;border-radius:2px}
.search span{left:12px;top:5px;font-size:5.5px;color:#aaa}
.search .btn{right:1px;top:1px;width:16px;height:16px;background:var(--gold);border-radius:2px}
.cart{left:578px;top:20px;width:53px;height:22px;background:var(--green);border:1px solid #b6e07a;border-radius:2px;color:#fff;font-size:5.5px;display:flex;align-items:center;justify-content:center;gap:2px}
.dots{left:94px;width:538px;height:0;border-top:2px dotted rgba(255,255,255,.2)}
.nav{left:95px;top:78px;color:#fff;font-size:7px;display:flex}
.nav span{margin-right:22px}
.slider{left:94px;top:146px;width:538px;height:216px;background:var(--white);border:1px solid #e2e2e2}
.slide{left:2px;top:2px;width:533px;height:185px;background:linear-gradient(90deg,#efe7d3,#f7f3ea 55%,#efe7d6)}
.slide h1{left:40px;top:45px;font-size:25px;font-weight:400;color:var(--text-red);letter-spacing:.3px}
.slide p{left:41px;top:81px;width:160px;font-size:7.6px;line-height:13.5px;color:#444}
.slide .more{left:40px;top:126px;font-size:7.6px;color:var(--gold)}
.slide .jars{left:226px;top:18px;width:252px;height:166px;background:radial-gradient(ellipse at 50% 55%,#8c5a3a 0 18%,#9fb2cf 30%,transparent 62%)}
.arrow-c{width:18px;height:18px;border-radius:50%;background:rgba(0,0,0,.06);top:84px}
.offer{left:0;top:186px;width:536px;height:28px;display:flex;align-items:center;justify-content:center;gap:18px;font-size:9.5px;color:#333}
.btn-gold{background:linear-gradient(#d6b23a,var(--gold-dark));color:#fff;border-radius:2px;font-size:5.5px;display:inline-flex;align-items:center;justify-content:center}
.offer .btn-gold{width:58px;height:18px;font-size:6px}
.section-title{left:94px;font-size:10.5px;color:var(--text-red);display:flex;align-items:center;width:538px}
.section-title .rule{flex:1;height:0;border-top:2px dotted #d4d4d4;margin:0 8px}
.pager{display:flex;gap:3px}
.pager i{width:11px;height:11px;background:var(--gold);border-radius:2px;display:block}
.card{width:125px;height:190px;background:var(--white)}
.card .photo{left:0;top:0;width:125px;height:66px}
.card .price{left:9px;top:75px;font-size:7px;color:#222}
.card .btn-gold{left:75px;top:72px;width:42px;height:12px}
.card .sep{left:0;top:92px;width:125px;border-top:1px solid #eee}
.card h3{left:9px;top:101px;font-size:7.5px;font-weight:400;color:var(--text-red)}
.card ul{left:9px;top:114px;list-style:none;font-size:5.6px;line-height:11.2px;color:#333}
.card .view{left:0;top:170px;width:125px;height:20px;border-top:2px solid var(--bg);font-size:7.6px;color:var(--gold);padding:4px 9px}
.tea-photo{left:95px;top:934px;width:81px;height:66px;background:linear-gradient(135deg,#2a1a1a,#7a1010 50%,#1d1d1d);border:2px solid #ccc}
.tea-text{left:198px;top:952px;width:400px;font-size:6.7px;line-height:11.2px;color:#333}
.footer{left:0;top:1022px;width:727px;height:148px;background:var(--white)}
.footer h4{font-size:9px;font-weight:400;color:#333}
.footer .col{top:24px}
.footer p{font-size:6.3px;line-height:10.3px;color:#444;margin-top:10px}
.archive div{font-size:6.5px;color:#333;width:110px;border-bottom:1px dotted #ccc;padding:6px 1px}
.contact div{font-size:6px;display:flex;align-items:center;gap:10px;margin-top:10px;color:#333}
.contact svg{width:14px;height:14px}
.news input{display:block;width:120px;height:20px;border:1px solid #eee;margin-top:6px;font:italic 7px "Lato",sans-serif;padding-left:7px;color:#333;background:#fff}
.subscribe{margin:13px 0 0 65px;width:55px;height:20px;background:var(--red);color:#fff;font-size:7px;display:flex;align-items:center;justify-content:center}
.social{display:flex;gap:8px;margin-top:8px}
.social i{width:9px;height:9px;border-radius:50%;background:#ccc;display:block}
.bottombar{left:0;top:1170px;width:727px;height:30px;background:#1f1f1f;color:#9a9a9a;font-size:5.8px}
.bottombar .l{left:97px;top:12px}
.bottombar .r{left:498px;top:12px}
</style>
</head>
<body>
<div class="abs topbar"><div class="abs links">My Account<span>|</span>Login<span>|</span>Register<span>|</span>Checkout</div></div>

<header class="abs header">
  <div class="abs brand"><span class="mark"></span><span class="name">LANXI</span></div>
  <div class="abs search"><span class="abs">Search...</span><span class="abs btn"><svg viewBox="0 0 16 16" width="16" height="16"><circle cx="7" cy="7" r="3.5" fill="none" stroke="#fff" stroke-width="1.5"/><path d="M9.5 9.5l3 3" stroke="#fff" stroke-width="1.5"/></svg></span></div>
  <div class="abs cart"><svg width="10" height="8" viewBox="0 0 10 8"><path d="M0 1h2l1.5 4.5h5L10 2H3" fill="none" stroke="#fff" stroke-width="1"/><circle cx="4" cy="7" r=".8" fill="#fff"/><circle cx="8" cy="7" r=".8" fill="#fff"/></svg>(0) ITEMS</div>
  <div class="abs dots" style="top:66px"></div>
  <nav class="abs nav"><span>HOME</span><span>ABOUT LANXI</span><span>COLLECTION</span><span>TEA HOUSE</span><span>CONTACT US</span></nav>
  <div class="abs dots" style="top:100px"></div>
</header>

<section class="abs slider">
  <div class="abs slide">
    <h1 class="abs">PORCELAIN JAR</h1>
    <p class="abs">Lorem ipsum dolor sit amet, consecte adipiscing elit. Fusce at justo eget lorem port titor tincidunt.</p>
    <span class="abs more">Check the Product &nbsp;›</span>
    <div class="abs jars" role="img" aria-label="Three porcelain and ceramic vases on display"></div>
    <span class="abs arrow-c" style="left:6px"></span>
    <span class="abs arrow-c" style="right:6px"></span>
  </div>
  <div class="abs offer">CHECK OUR AMAZING OFFERS, VISIT OUR STORE NOW <span class="btn-gold">VISIT THE STORE</span></div>
</section>

<div class="abs section-title" style="top:388px">RECENT PRODUCTS<span class="rule"></span><span class="pager"><i></i><i></i></span></div>

<article class="abs card" style="left:97px;top:426px"><div class="abs photo" role="img" aria-label="Dragon porcelain jar" style="background:radial-gradient(circle at 50% 55%,#c99a2a 0 25%,#111 50%)"></div><span class="abs price">$280AUD</span><span class="abs btn-gold">ADD TO CART</span><span class="abs sep"></span><h3 class="abs">Dragon Porcelain Jar</h3><ul class="abs"><li>Origin: Jingdezhen</li><li>Style: Ming</li><li>Technique: hand-made, high fire</li><li>Weight: 100g</li></ul><div class="abs view">View the Product ›</div></article>
<article class="abs card" style="left:234px;top:426px"><div class="abs photo" role="img" aria-label="Bronze vessel" style="background:linear-gradient(#b2a06c,#6f6a4c)"></div><span class="abs price">$280AUD</span><span class="abs btn-gold">ADD TO CART</span><span class="abs sep"></span><h3 class="abs">Bronze</h3><ul class="abs"><li>Origin: Jingdezhen</li><li>Style: Ming</li><li>Technique: hand-made, high fire</li><li>Weight: 100g</li></ul><div class="abs view">View the Product ›</div></article>
<article class="abs card" style="left:370px;top:426px"><div class="abs photo" role="img" aria-label="Bronze ding cauldron" style="background:radial-gradient(circle at 50% 50%,#4a5558 0 28%,#c3c6c6 60%)"></div><span class="abs price">$280AUD</span><span class="abs btn-gold">ADD TO CART</span><span class="abs sep"></span><h3 class="abs">Bronze</h3><ul class="abs"><li>Origin: Jingdezhen</li><li>Style: Ming</li><li>Technique: hand-made, high fire</li><li>Weight: 100g</li></ul><div class="abs view">View the Product ›</div></article>
<article class="abs card" style="left:507px;top:426px"><div class="abs photo" role="img" aria-label="Terra cotta warrior figure" style="background:radial-gradient(circle at 55% 55%,#a68a6a 0 25%,#2a241f 60%)"></div><span class="abs price">$280AUD</span><span class="abs btn-gold">ADD TO CART</span><span class="abs sep"></span><h3 class="abs">Terra Cotta</h3><ul class="abs"><li>Origin: Jingdezhen</li><li>Style: Ming</li><li>Technique: hand-made, high fire</li><li>Weight: 100g</li></ul><div class="abs view">View the Product ›</div></article>

<div class="abs section-title" style="top:646px">FEATURED PRODUCTS<span class="rule"></span><span class="pager"><i></i><i></i></span></div>

<article class="abs card" style="left:97px;top:684px"><div class="abs photo" role="img" aria-label="Chinese calligraphy scroll" style="background:linear-gradient(90deg,#d8d6cf,#bfbcb4)"></div><span class="abs price">$280AUD</span><span class="abs btn-gold">ADD TO CART</span><span class="abs sep"></span><h3 class="abs">Painting &amp; Calligraphy</h3><ul class="abs"><li>Origin: Jingdezhen</li><li>Style: Ming</li><li>Technique: hand-made, high fire</li><li>Weight: 100g</li></ul><div class="abs view">View the Product ›</div></article>
<article class="abs card" style="left:234px;top:684px"><div class="abs photo" role="img" aria-label="Framed red paper cut artwork" style="background:radial-gradient(circle at 50% 55%,#c0392b 0 22%,#f1ece4 32%,#222 80%)"></div><span class="abs price">$280AUD</span><span class="abs btn-gold">ADD TO CART</span><span class="abs sep"></span><h3 class="abs">Folk's PaperCut</h3><ul class="abs"><li>Origin: Jingdezhen</li><li>Style: Ming</li><li>Technique: hand-made, high fire</li><li>Weight: 100g</li></ul><div class="abs view">View the Product ›</div></article>
<article class="abs card" style="left:370px;top:684px"><div class="abs photo" role="img" aria-label="Traditional Chinese landscape painting" style="background:linear-gradient(#e4e0d4,#9aa097)"></div><span class="abs price">$10AUD</span><span class="abs btn-gold">ADD TO CART</span><span class="abs sep"></span><h3 class="abs">Painting</h3><ul class="abs"><li>Origin: Painting</li><li>Style: Ming</li><li>Technique: hand-made, high fire</li><li>Weight: 100g</li></ul><div class="abs view">View the Product ›</div></article>
<article class="abs card" style="left:507px;top:684px"><div class="abs photo" role="img" aria-label="Porcelain tea set with cups" style="background:linear-gradient(#9c8a7a,#e8e2dc)"></div><span class="abs price">$280AUD</span><span class="abs btn-gold">ADD TO CART</span><span class="abs sep"></span><h3 class="abs">Tea Pot's</h3><ul class="abs"><li>Origin: Jingdezhen</li><li>Style: Ming</li><li>Technique: hand-made, high fire</li><li>Weight: 100g</li></ul><div class="abs view">View the Product ›</div></article>

<div class="abs section-title" style="top:905px;left:95px;width:537px">TEA HOUSE<span class="rule"></span></div>
<div class="abs tea-photo" role="img" aria-label="Tea house interior with red lanterns"></div>
<p class="abs tea-text">A genuine Chinese cultural experience is incomplete without Chinese tea, which has been a significant part of the oriental culture and lifestyle. We handpick a variety of premium Chinese tea, with profound taste and tremendous inner-health benefit. &nbsp;We look forward to seeing you here and sharing with you a genuine experience of Chinese tea culture.</p>

<footer class="abs footer">
  <div class="abs col" style="left:95px;width:110px">
    <h4>LITTLE ABOUT US</h4>
    <p>Sed posuere consectetur est at. Nulla vitae elit libero, a pharetra. Lorem ipsum dolor sit amet, conse ctetuer adipiscing elit.</p>
    <h4 style="margin-top:14px">FOLLOW US</h4>
    <div class="social"><i></i><i></i><i></i><i></i><i></i><i></i></div>
  </div>
  <div class="abs col archive" style="left:237px">
    <h4>ARCHIVES</h4>
    <div style="margin-top:4px">March 2014</div><div>February 2014</div><div>January 2014</div><div style="border:0">December 2013</div>
  </div>
  <div class="abs col contact" style="left:378px">
    <h4>CONTACT US</h4>
    <div><svg viewBox="0 0 14 14"><rect x="1" y="3" width="12" height="8" fill="none" stroke="#999"/><path d="M1 3l6 5 6-5" fill="none" stroke="#999"/></svg>info@lanxi-gallery.com</div>
    <div><svg viewBox="0 0 14 14"><path d="M3 2l2 0 1 3-1.5 1a7 7 0 0 0 3.5 3.5l1-1.5 3 1v2a1 1 0 0 1-1 1A10 10 0 0 1 2 3a1 1 0 0 1 1-1z" fill="#999"/></svg>1800 xxx xxx</div>
    <div><svg viewBox="0 0 14 14"><rect x="4" y="1" width="7" height="12" rx="1" fill="#999"/><rect x="5" y="3" width="5" height="7" fill="#fff"/></svg>1800 xxx xxx</div>
  </div>
  <div class="abs col news" style="left:512px">
    <h4>SIGN TO NEWSLETTER</h4>
    <input value="Name" readonly style="margin-top:10px"><input value="Email" readonly>
    <div class="subscribe">SUBSCRIBE</div>
  </div>
</footer>

<div class="abs bottombar">
  <div class="abs l">HOME &nbsp;| &nbsp;ABOUT LANXI &nbsp;| &nbsp;COLLECTION &nbsp;| &nbsp;TEA HOUSE &nbsp;| &nbsp;CONTACT US</div>
  <div class="abs r">Copy right @2014 lanxi | All Rights Reserved</div>
</div>
</body>
</html>
```